MARBLED SPARROW WEB DESIGN PROJECT

We are a brand new company called "Marbled Sparrow" which specialise in one-off Vintage Clothing. We would like somebody to design a web page which will be the sole income for our company. Our main aim is to have an easy searchable website which is user friendly. The key to the website is to target people who do not like the idea of op-shopping but love vintage clothes - this website will be the answer.
Updates

This website will need to be coded to work with Tin Lantern - Please read this before you start. https://help.tinlantern.example/articles/Public/How-do-I-create-custom-template-files-for-my-store

Hi everyone, Just want to make note that the this website is for young people. Just so people a clear I want modern young people dressed in Vintage clothes as this is that reality and what they would like to see. Not people dressed like they are going to a fancy dress party, i.e. dresses like it was that era. Thanks Mirela

Coding

Coded - Design and coding required

```html
<!DOCTYPE html>
<html lang="en">
<head>
<meta charset="utf-8">
<title>Marbled Sparrow — Unique Vintage Fashion and Accessories</title>
<link rel="stylesheet" href="https://fonts.googleapis.com/css2?family=Allura&family=Lato:wght@400;700;900&family=Oswald:wght@500&display=swap">
<style>
:root{
  --cream:#fdf9ea;
  --white:#ffffff;
  --teal:#1eaac6;
  --teal-dark:#1593ad;
  --pink:#f05a6a;
  --ink:#3a3a3a;
  --muted:#777777;
  --line:#d5d5d5;
  --sage:#97a395;
  --paper:#f4ecd0;
}
*{box-sizing:border-box;margin:0;padding:0}
html,body{width:735px;height:1200px;overflow:hidden}
body{background:var(--cream);font-family:'Lato',sans-serif;color:var(--ink);position:relative}
a{color:inherit;text-decoration:none}
.page{position:absolute;left:51px;top:10px;width:633px;height:1176px;background:var(--white)}
.abs{position:absolute}

/* header */
.utility{position:absolute;top:21px;left:454px;display:flex;gap:12px;font-size:8px;color:var(--ink)}
.utility span{display:flex;align-items:center;gap:4px}
.brand{position:absolute;left:28px;top:32px}
.brand-name{font-size:19px;font-weight:400;color:var(--pink);letter-spacing:.5px}
.brand-tag{font-size:7.5px;font-weight:700;margin-top:3px}
.search{position:absolute;left:289px;top:37px;width:148px;height:20px}
.search input{position:absolute;left:8px;top:3px;width:120px;height:14px;border:0;border-radius:7px;background:var(--white);font:8px 'Lato',sans-serif;color:var(--pink);padding-left:7px}
.btn{position:absolute;top:36px;height:22px;width:72px;color:var(--white);font-size:10px;display:flex;align-items:center;justify-content:center}
.btn svg{position:absolute;inset:0}
.btn span{position:relative}

/* nav */
.nav{position:absolute;left:18px;top:77px;width:597px;height:36px;background:var(--teal);display:flex;align-items:center;font-size:8px;letter-spacing:.8px;color:var(--white)}
.nav-home{width:42px;height:36px;background:var(--teal-dark);display:flex;align-items:center;justify-content:center}
.nav-item{position:absolute;top:0;height:36px;display:flex;align-items:center;justify-content:center;white-space:nowrap}
.nav-item.active{background:var(--white);color:var(--teal)}
.nav-divider{position:absolute;top:0;width:1px;height:36px;background:rgba(255,255,255,.35)}
.ship-note{position:absolute;left:409px;top:4px;width:184px;height:30px;background:linear-gradient(90deg,#fbf4e0 55%,#f0d7c4);padding:5px 7px;color:var(--ink);letter-spacing:0;white-space:nowrap}
.ship-note b{font-weight:900}
.ship-note p{font-size:7.3px;line-height:1.1}
.ship-note small{font-size:6px;display:block}

/* hero */
.hero{position:absolute;left:18px;top:124px;width:597px;height:171px;border-radius:3px;overflow:hidden;
  background:linear-gradient(90deg,#7d806c 0%,#d9d9cf 12%,#8a8d78 22%,#e2e0d8 32%,#8c8f7a 46%,#ece9e0 60%,#7f8470 72%,#d7d6cc 86%,#7b806b 100%)}
.hero-title{position:absolute;top:30px;width:100%;text-align:center;font-size:24px;font-weight:700;color:var(--white);letter-spacing:1px}
.hero-sub{position:absolute;top:70px;width:100%;text-align:center;font-size:8.5px;font-weight:700;line-height:1.45;color:var(--white)}
.hero-tag{position:absolute;left:274px;top:105px;width:39px;height:20px;background:var(--teal);color:var(--white);font-size:10px;font-weight:700;display:flex;align-items:center;justify-content:center;transform:rotate(-7deg)}
.hero-dots{position:absolute;top:152px;left:279px;display:flex;gap:4px}
.hero-dots i{width:4px;height:4px;border-radius:50%;border:1px solid var(--white)}
.hero-dots i:first-child{background:var(--white)}
.hero-arrow{position:absolute;top:90px}

/* featured */
.section-title{position:absolute;left:17px;top:305px;font-size:15.5px;color:var(--teal)}
.section-rule{position:absolute;left:18px;top:328px;width:597px;height:1px;background:var(--line)}
.section-rule::before{content:"";position:absolute;left:0;top:-1px;width:130px;height:1px;background:var(--pink)}
.product{position:absolute;top:344px;width:138px;height:202px;border:1px solid #e3e3e3;background:var(--white)}
.product-photo{height:148px}
.badge{position:absolute;left:1px;top:8px;padding:3px 5px;font-size:6.5px;color:var(--white);letter-spacing:.5px}
.product-title{position:absolute;left:6px;top:155px;font-size:9px;letter-spacing:.6px}
.product-desc{position:absolute;left:6px;top:166px;font-size:6.5px;color:var(--pink);letter-spacing:.4px}
.product-desc.teal{color:var(--teal)}
.product-bar{position:absolute;left:0;bottom:0;width:100%;height:25px;border-top:1px solid #e3e3e3;display:flex}
.product-bar .tool{width:28.7px;border-right:1px solid #e3e3e3;display:flex;align-items:center;justify-content:center}
.price{flex:1;background:var(--pink);color:var(--white);font-size:11px;display:flex;align-items:center;justify-content:center}
.price.teal{background:var(--teal)}
.price sup{font-size:6px}

.tile{position:absolute;top:563px;width:189px;height:127px}

/* quote */
.quote-mark{position:absolute;left:25px;top:712px;font-size:26px;color:#cccccc;font-family:Georgia,serif}
.quote{position:absolute;left:18px;top:720px;width:597px;text-align:center;font-family:'Allura',cursive;font-size:17px;line-height:17px;color:var(--ink);white-space:nowrap}

/* newsletter */
.community{position:absolute;left:18px;top:774px;width:597px;height:101px;background:var(--sage);overflow:hidden}
.community-photo{position:absolute;left:0;top:0;width:165px;height:101px;background:linear-gradient(90deg,#d9d3bf 0%,#c8c7b2 50%,rgba(151,163,149,0) 100%)}
.community-title{position:absolute;left:163px;top:12px;font-family:'Oswald',sans-serif;font-size:17px;color:var(--white);letter-spacing:-.3px}
.community-sub{position:absolute;left:163px;top:38px;font-size:12px;color:var(--white)}
.signup{position:absolute;left:162px;top:63px;width:240px;height:22px}
.signup-field{position:absolute;left:7px;top:3px;width:185px;height:16px;border-radius:8px;background:var(--paper);font-size:7px;color:#a59c7c;display:flex;align-items:center;padding-left:22px}
.signup-join{position:absolute;left:198px;top:4px;font-size:9px;color:var(--white)}
.social{position:absolute;top:61px;width:25px;height:25px;border-radius:50%;background:var(--paper)}

/* footer */
.rule{position:absolute;left:18px;width:597px;height:1px;background:var(--line)}
.foot-col{position:absolute;top:925px}
.foot-col h3{font-size:11px;font-weight:400;letter-spacing:.2px;margin-bottom:19px}
.foot-col li{list-style:none;font-size:7.5px;color:var(--ink);height:15.2px}
.trust{position:absolute;left:18px;top:1082px;width:28px;height:22px;background:var(--teal)}
.pay-strip{position:absolute;left:152px;top:1076px;width:287px;height:33px;background:#f1f1f1;display:flex;align-items:center;justify-content:space-around;font-size:11px;font-weight:700;color:#2a4a8f}
.copyright{position:absolute;left:29px;top:1137px;font-size:7px}
</style>
</head>
<body>
<main class="page">

  <header>
    <nav class="utility" aria-label="Account">
      <span><svg width="10" height="9" viewBox="0 0 10 9"><path d="M0 1h2l1.5 5h5L10 2H3" fill="none" stroke="#1eaac6" stroke-width="1.2"/><circle cx="4" cy="8" r=".9" fill="#1eaac6"/><circle cx="8" cy="8" r=".9" fill="#1eaac6"/></svg>View Cart</span>
      <span><svg width="9" height="9" viewBox="0 0 9 9"><rect x="0" y="2" width="9" height="2.5" fill="#f05a6a"/><rect x="1" y="4.5" width="7" height="4.5" fill="#f05a6a"/><rect x="4" y="2" width="1" height="7" fill="#fff"/></svg>Wish List</span>
      <span><svg width="9" height="9" viewBox="0 0 9 9"><circle cx="4.5" cy="4.5" r="4.5" fill="#1eaac6"/><text x="4.5" y="7" font-size="7" text-anchor="middle" fill="#fff" font-family="Lato">?</text></svg>Help</span>
    </nav>

    <div class="brand">
      <div class="brand-name">Marbled Sparrow</div>
      <div class="brand-tag">Unique Vintage Fashion and Accessories</div>
    </div>

    <div class="search">
      <svg width="148" height="20" viewBox="0 0 148 20" class="abs"><path d="M4 0H144L148 4V16L144 20H4L0 16V4Z" fill="#f05a6a"/><circle cx="133" cy="9" r="3.5" fill="none" stroke="#fff" stroke-width="1.3"/><path d="M135.5 11.5l3 3" stroke="#fff" stroke-width="1.3"/></svg>
      <input type="text" value="Search" aria-label="Search">
    </div>

    <a class="btn" style="left:449px">
      <svg width="72" height="22" viewBox="0 0 72 22"><path d="M0 0H72L68 11L72 22H0Z" fill="#1eaac6"/><path d="M66 2L63 11L66 20" fill="none" stroke="#fff" stroke-width=".8"/></svg>
      <span>Sign Up</span>
    </a>
    <a class="btn" style="left:530px">
      <svg width="72" height="22" viewBox="0 0 72 22"><path d="M0 0H72L68 11L72 22H0L4 11Z" fill="#f05a6a"/><path d="M66 2L63 11L66 20" fill="none" stroke="#fff" stroke-width=".8"/></svg>
      <span>Login</span>
    </a>
  </header>

  <nav class="nav" aria-label="Main">
    <a class="nav-home" aria-label="Home"><svg width="11" height="10" viewBox="0 0 11 10"><path d="M5.5 0L11 5H9.5V10H6.5V7H4.5V10H1.5V5H0Z" fill="#fff"/></svg></a>
    <span class="nav-divider" style="left:42px"></span>
    <a class="nav-item" style="left:42px;width:77px">WOMEN</a>
    <span class="nav-divider" style="left:119px"></span>
    <a class="nav-item active" style="left:119px;width:65px">MEN</a>
    <a class="nav-item" style="left:250px;width:76px">STYLE TIPS</a>
    <a class="nav-item" style="left:337px;width:44px">FAQS</a>
    <div class="ship-note">
      <p>Orders over $100 will receive <b>FREE SHIPPING</b></p>
      <small>Find out more about delivery &amp; shipping &gt;&gt;&gt;</small>
    </div>
  </nav>

  <section class="hero" role="img" aria-label="Summer sale banner: models in white vintage lace wedding dresses">
    <svg class="hero-arrow" style="left:14px" width="6" height="10" viewBox="0 0 6 10"><path d="M5 1L1 5L5 9" fill="none" stroke="#fff" stroke-width="1.2"/></svg>
    <svg class="hero-arrow" style="right:14px" width="6" height="10" viewBox="0 0 6 10"><path d="M1 1L5 5L1 9" fill="none" stroke="#fff" stroke-width="1.2"/></svg>
    <h1 class="hero-title">SUMMER SALES</h1>
    <p class="hero-sub">It was some time before he obtained any answer, and<br>the reply, when made, was unpropitious.</p>
    <div class="hero-tag">- 50%</div>
    <div class="hero-dots"><i></i><i></i><i></i><i></i></div>
  </section>

  <h2 class="section-title">Featured Products</h2>
  <div class="section-rule"></div>

  <article class="product" style="left:18px">
    <div class="product-photo" role="img" aria-label="Model in black and white polka dot swing dress" style="background:linear-gradient(180deg,#f7f7f7,#e9e9e9 60%,#d8d8d8)"></div>
    <span class="badge" style="background:var(--pink)">20% OFF</span>
    <div class="product-title">Product Title here</div>
    <div class="product-desc">Short Description here</div>
    <div class="product-bar">
      <span class="tool"><svg width="9" height="7" viewBox="0 0 9 7"><path d="M0 2H8M6 0L8 2L6 4M9 5H1M3 3L1 5L3 7" fill="none" stroke="#aaa" stroke-width=".8"/></svg></span>
      <span class="tool"><svg width="8" height="8" viewBox="0 0 8 8"><rect x="0" y="1" width="8" height="2" fill="#aaa"/><rect x="1" y="3" width="6" height="5" fill="#aaa"/></svg></span>
      <span class="tool"><svg width="9" height="8" viewBox="0 0 10 9"><path d="M0 1h2l1.5 5h5L10 2H3" fill="none" stroke="#aaa" stroke-width="1"/></svg></span>
      <span class="price">$99.<sup>00</sup></span>
    </div>
  </article>

  <article class="product" style="left:171px">
    <div class="product-photo" role="img" aria-label="Model in purple halter neck vintage dress" style="background:linear-gradient(180deg,#f7f7f7,#e3dde5 60%,#cfc3d3)"></div>
    <div class="product-title">Product Title here</div>
    <div class="product-desc">Short Description here</div>
    <div class="product-bar">
      <span class="tool"><svg width="9" height="7" viewBox="0 0 9 7"><path d="M0 2H8M6 0L8 2L6 4M9 5H1M3 3L1 5L3 7" fill="none" stroke="#aaa" stroke-width=".8"/></svg></span>
      <span class="tool"><svg width="8" height="8" viewBox="0 0 8 8"><rect x="0" y="1" width="8" height="2" fill="#aaa"/><rect x="1" y="3" width="6" height="5" fill="#aaa"/></svg></span>
      <span class="tool"><svg width="9" height="8" viewBox="0 0 10 9"><path d="M0 1h2l1.5 5h5L10 2H3" fill="none" stroke="#aaa" stroke-width="1"/></svg></span>
      <span class="price">$99.<sup>00</sup></span>
    </div>
  </article>

  <article class="product" style="left:325px">
    <div class="product-photo" role="img" aria-label="Model in black lace sleeve cocktail dress" style="background:linear-gradient(180deg,#f7f7f7,#e6e6e6 60%,#cfcfcf)"></div>
    <span class="badge" style="background:var(--teal)">New</span>
    <div class="product-title">Product Title here</div>
    <div class="product-desc teal">Short Description here</div>
    <div class="product-bar">
      <span class="tool"><svg width="9" height="7" viewBox="0 0 9 7"><path d="M0 2H8M6 0L8 2L6 4M9 5H1M3 3L1 5L3 7" fill="none" stroke="#aaa" stroke-width=".8"/></svg></span>
      <span class="tool"><svg width="8" height="8" viewBox="0 0 8 8"><rect x="0" y="1" width="8" height="2" fill="#aaa"/><rect x="1" y="3" width="6" height="5" fill="#aaa"/></svg></span>
      <span class="tool"><svg width="9" height="8" viewBox="0 0 10 9"><path d="M0 1h2l1.5 5h5L10 2H3" fill="none" stroke="#aaa" stroke-width="1"/></svg></span>
      <span class="price teal">$99.<sup>00</sup></span>
    </div>
  </article>

  <article class="product" style="left:478px">
    <div class="product-photo" role="img" aria-label="Model in navy blue swing dress with white belt" style="background:linear-gradient(180deg,#f7f7f7,#e1e3ea 60%,#c6cbd9)"></div>
    <div class="product-title">Product Title here</div>
    <div class="product-desc">Short Description here</div>
    <div class="product-bar">
      <span class="tool"><svg width="9" height="7" viewBox="0 0 9 7"><path d="M0 2H8M6 0L8 2L6 4M9 5H1M3 3L1 5L3 7" fill="none" stroke="#aaa" stroke-width=".8"/></svg></span>
      <span class="tool"><svg width="8" height="8" viewBox="0 0 8 8"><rect x="0" y="1" width="8" height="2" fill="#aaa"/><rect x="1" y="3" width="6" height="5" fill="#aaa"/></svg></span>
      <span class="tool"><svg width="9" height="8" viewBox="0 0 10 9"><path d="M0 1h2l1.5 5h5L10 2H3" fill="none" stroke="#aaa" stroke-width="1"/></svg></span>
      <span class="price">$99.<sup>00</sup></span>
    </div>
  </article>

  <div class="tile" style="left:18px;background:linear-gradient(135deg,#8a6f58,#b2624f 50%,#5d4a3c)" role="img" aria-label="Red vintage handbag on a trench coat"></div>
  <div class="tile" style="left:222px;background:linear-gradient(135deg,#2c2436,#4a3a48 50%,#6b5540)" role="img" aria-label="Pearl necklace and jewelled brooch on dark velvet"></div>
  <div class="tile" style="left:426px;background:linear-gradient(135deg,#3a3f4e,#7a6d54 55%,#b59a5c)" role="img" aria-label="Gold vintage wristwatch on a wrist"></div>

  <span class="quote-mark">&ldquo;</span>
  <p class="quote">Marbled Sparrow is all about being different. That’s way all of our clothes are unique,<br>so you can be dazzling different</p>

  <section class="community">
    <div class="community-photo" role="img" aria-label="Woman in a cream lace vintage dress"></div>
    <h2 class="community-title">BECOME PART OF OUR COMMUNITY</h2>
    <p class="community-sub">Sign up to our newsletter:</p>
    <div class="signup">
      <svg width="240" height="22" viewBox="0 0 240 22" class="abs"><path d="M4 0H236L240 11L236 22H4L0 11Z" fill="#6f7b6d"/></svg>
      <div class="signup-field">
        <svg width="10" height="7" viewBox="0 0 10 7" style="position:absolute;left:7px"><rect x=".5" y=".5" width="9" height="6" fill="none" stroke="#8c8466"/><path d="M.5 .5L5 4L9.5 .5" fill="none" stroke="#8c8466"/></svg>
        hello@marbledsparrow.example
      </div>
      <span class="signup-join">Join &raquo;</span>
    </div>
    <span class="social" style="left:421px"></span>
    <span class="social" style="left:450px"></span>
    <span class="social" style="left:479px"></span>
    <span class="social" style="left:508px"></span>
  </section>

  <div class="rule" style="top:902px"></div>

  <footer>
    <div class="foot-col" style="left:29px">
      <h3>MARBLED SPARROW</h3>
      <ul><li>About us</li><li>Terms of use</li><li>Privacy policy</li><li>Press</li></ul>
    </div>
    <div class="foot-col" style="left:172px">
      <h3>CONNECT WITH US</h3>
      <ul><li>Contact us</li><li>My Account</li><li>Style Tips</li><li>FAQs</li><li>Shipping</li><li>Track your order</li><li>Size chart</li></ul>
    </div>
    <div class="foot-col" style="left:293px">
      <h3>SHOP BY POPULAR CATEGORIES</h3>
      <ul><li>Men</li><li>Women</li><li>Accessories</li><li>Bags</li><li>Shoes</li></ul>
    </div>
    <div class="foot-col" style="left:403px">
      <h3>&nbsp;</h3>
      <ul><li>50s</li><li>60s</li><li>70s</li><li>80s</li><li>90s</li></ul>
    </div>

    <span class="trust" aria-label="Security certificate badge"></span>
    <div class="pay-strip">
      <span>Swiftpay</span><span>Penny Post</span><span>Carta</span><span>Orbit Card</span>
    </div>

    <div class="rule" style="top:1124px"></div>
    <p class="copyright">©Marbled Sparrow. All Prices are in AUD.</p>
    <div class="rule" style="top:1158px"></div>
  </footer>

</main>
</body>
</html>
```